Website - Lulu Fizz Pop
Charity Website
Project: Website - Lulu Fizz Pop
Website - Lulu Fizz Pop - Fund Raising
Creative Brief
Fund Raising
http://www.lulufizzpop.example/
This is a website and charity designed to help support Brest Cancer victims. It is designed to incorporate fighting breast cancer, God and one favorite southern activity of shooting skeet.
Below are some of the things we like, also some notes like the color Pink used is PMS213. We also have an idea of a HTML5 intro / top of the home page that will last 5 seconds or so. It will have a shotgun shoot with the sound, then smoke comes out of the barrell and turns into the Lulu Fizz Pop logo. -Pink used in the logo is "PMS 213" Objects to incorporate: -Pink Shotshell (aka Shotgun shell) -Over and Under Shotgun -Pink Clay Targets (also called pigeons, skeet) (when you do a Web search using "Sporting Clays" you can find a lot of above objects) -Over and Under shotgun going off busting a PINK clay target that swirls into the logo with smoke coming from barrels swirling into pages listed at the top pages (5-10 secs intro) -Sound: pumping gun and shot being fired (like this on ClipTube) https://www.cliptube.example/watch?v=k27WmpRnd4s List of websites wanting us (give domains): www.brindlegoods.example www.ridgemarkers.example www.cobaltpinecrafts.example Unique Websites (coloring, layout, etc.): -dustyloomhall.example.au (like the faded photo background gray look) -www.site-motion-kits.example/marsh_lodge_mediapanel_motion_kits_471902236.php (like the "high-end" look of this... simple to navigate, yet intelligent-looking) -www.harlowtrailgear.example/new/default.asp. (Like the gray background with the fade in the center) Ideas from charitable websites as for donations and ideas (give domains): Charity Websites -www.QuietHarbors.example (like the donate button and the ease of functionality-easy of navigation) -www.RoofTogether.example (like the simplicity and ease of navigation)
Modern
Pink - PMS - 213
Black
Optional
left side
-Pink used in the logo is "PMS 213" Objects to incorporate: -Pink Shotshell (aka Shotgun shell) -Over and Under Shotgun -Pink Clay Targets (also called pigeons, skeet) (when you do a Web search using "Sporting Clays" you can find a lot of above objects) -Over and Under shotgun going off busting a PINK clay target that swirls into the logo with smoke coming from barrels swirling into pages listed at the top pages (5-10 secs intro) -Sound: pumping gun and shot being fired (like this on ClipTube) https://www.cliptube.example/watch?v=k27WmpRnd4s List of websites wanting us (give domains): www.brindlegoods.example www.ridgemarkers.example www.cobaltpinecrafts.example Unique Websites (coloring, layout, etc.): -dustyloomhall.example.au (like the faded photo background gray look) -www.site-motion-kits.example/marsh_lodge_mediapanel_motion_kits_471902236.php (like the "high-end" look of this... simple to navigate, yet intelligent-looking) -www.harlowtrailgear.example/new/default.asp. (Like the gray background with the fade in the center) Ideas from charitable websites as for donations and ideas (give domains): Charity Websites -www.QuietHarbors.example (like the donate button and the ease of functionality-easy of navigation) -www.RoofTogether.example (like the simplicity and ease of navigation)

```html
<!DOCTYPE html>
<html lang="en">
<head>
<meta charset="utf-8">
<title>Lulu Fizz Pop</title>
<link rel="stylesheet" href="https://fonts.googleapis.com/css2?family=Rye&family=Lato:wght@400;700&display=swap">
<style>
  :root {
    --bg-dark: #2a0d06;
    --bg-mid: #6e2a12;
    --bg-light: #8c3c1c;
    --wood-dark: #3a1a0a;
    --wood-mid: #6b3515;
    --wood-light: #8a4a20;
    --frame: #b07a44;
    --cream: #f6e7c4;
    --tan: #d8a867;
    --tan-dark: #a86c34;
    --ink: #2b1206;
    --white: #ffffff;
    --footer: #1e0c05;
  }
  * { margin: 0; padding: 0; box-sizing: border-box; }
  html, body { width: 1200px; height: 761px; overflow: hidden; }
  body {
    position: relative;
    font-family: "Lato", sans-serif;
    background: var(--bg-dark);
  }
  .backdrop {
    position: absolute; inset: 0;
    background:
      radial-gradient(ellipse at 50% 40%, var(--bg-light) 0%, var(--bg-mid) 45%, var(--bg-dark) 100%);
  }
  .panel {
    position: absolute;
    left: 163px; top: 53px; width: 874px; height: 691px;
    border: 8px solid var(--frame);
    border-radius: 6px;
    background: linear-gradient(90deg, var(--wood-dark) 0%, var(--wood-mid) 25%, var(--wood-light) 50%, var(--wood-mid) 75%, var(--wood-dark) 100%);
    box-shadow: 0 0 30px rgba(0,0,0,.7), inset 0 0 60px rgba(0,0,0,.6);
  }
  .brand {
    position: absolute;
    left: 480px; top: 19px; width: 240px; height: 160px;
    display: flex; align-items: center; justify-content: center;
    font-family: "Rye", serif;
    font-size: 38px; line-height: 1;
    color: var(--ink);
    background: var(--tan);
    border-radius: 4px;
  }
  .donate {
    position: absolute;
    left: 828px; top: 103px; width: 115px; height: 36px;
    display: flex; align-items: center; justify-content: center;
    font-family: "Lato", sans-serif; font-weight: 700;
    font-size: 19px; letter-spacing: 1px;
    color: var(--ink);
    background: var(--tan);
    border: 2px solid var(--tan-dark);
    border-radius: 4px;
  }
  .sound {
    position: absolute;
    left: 955px; top: 103px; width: 48px; height: 36px;
    background: var(--tan);
    border: 2px solid var(--tan-dark);
    border-radius: 4px;
    display: flex; align-items: center; justify-content: center;
  }
  .rifle {
    position: absolute;
    left: 204px; top: 223px; width: 343px; height: 70px;
    background: linear-gradient(90deg, #5a2a10 0%, #7a4a22 35%, #333 55%, #555 100%);
    border-radius: 6px;
    opacity: .85;
  }
  .main-nav {
    position: absolute;
    left: 284px; top: 286px; width: 320px;
    list-style: none;
    text-align: center;
  }
  .main-nav li {
    height: 45.6px;
    display: flex; align-items: center; justify-content: center;
    font-family: "Rye", serif;
    font-size: 26px;
    color: var(--cream);
    text-shadow: 2px 2px 0 var(--ink);
    letter-spacing: 1px;
  }
  .main-nav .current { gap: 8px; }
  .main-nav .current span {
    background: var(--tan);
    color: var(--ink);
    text-shadow: none;
    padding: 2px 16px;
    border-radius: 10px;
  }
  .video {
    position: absolute;
    left: 598px; top: 228px; width: 408px; height: 245px;
    background: #000;
  }
  .video-scene {
    position: absolute; left: 0; top: 0; width: 408px; height: 216px;
    background: linear-gradient(180deg, #6e8a4a 0%, #8fa060 45%, #b3a070 75%, #7d6a40 100%);
  }
  .play {
    position: absolute; left: 178px; top: 82px;
  }
  .video-controls {
    position: absolute; left: 0; bottom: 0; width: 408px; height: 29px;
    background: #1b1b1b;
    display: flex; align-items: center; gap: 10px; padding: 0 10px;
    font-size: 11px; color: #ddd;
  }
  .progress { flex: 1; height: 3px; background: #555; }
  .event-copy {
    position: absolute;
    left: 598px; top: 488px; width: 410px;
    font-size: 15.5px; line-height: 1.35;
    color: var(--white);
  }
  .footer {
    position: absolute;
    left: 171px; top: 696px; width: 858px; height: 40px;
    background: var(--footer);
    display: flex; align-items: center; justify-content: space-between;
    padding: 0 10px 0 8px;
  }
  .copyright { font-size: 12px; color: var(--cream); }
  .social { display: flex; gap: 12px; }
  .social span {
    width: 20px; height: 20px; border-radius: 50%;
    background: var(--tan);
  }
</style>
</head>
<body>
  <div class="backdrop" role="img" aria-label="Grungy rust and brown textured backdrop with dark tree silhouettes"></div>

  <div class="panel"></div>

  <div class="brand">Lulu Fizz Pop</div>

  <div class="donate">DONATE</div>
  <div class="sound" aria-label="Sound">
    <svg width="22" height="18" viewBox="0 0 22 18">
      <path d="M2 6h4l6-5v16l-6-5H2z" fill="#2b1206"/>
      <path d="M15 5q3 4 0 8M17.5 2.5q5 6.5 0 13" stroke="#2b1206" stroke-width="2" fill="none"/>
    </svg>
  </div>

  <div class="rifle" role="img" aria-label="Lever-action rifle illustration"></div>

  <ul class="main-nav">
    <li class="current">
      <svg width="46" height="16" viewBox="0 0 46 16"><path d="M0 8l10-7v4h36v6H10v4z" fill="#f6e7c4"/></svg>
      <span>HOME</span>
      <svg width="46" height="16" viewBox="0 0 46 16"><path d="M46 8L36 1v4H0v6h36v4z" fill="#f6e7c4"/></svg>
    </li>
    <li>ABOUT US</li>
    <li>OUR STORY</li>
    <li>NEWS</li>
    <li>DONATIONS</li>
    <li>USEFUL LINKS</li>
    <li>CONTACT US</li>
  </ul>

  <div class="video">
    <div class="video-scene" role="img" aria-label="Video still of two shooters aiming shotguns beside hay bales in a green field"></div>
    <svg class="play" width="52" height="52" viewBox="0 0 52 52">
      <circle cx="26" cy="26" r="26" fill="rgba(0,0,0,.7)"/>
      <path d="M20 15l18 11-18 11z" fill="#fff"/>
    </svg>
    <div class="video-controls">
      <svg width="10" height="12" viewBox="0 0 10 12"><path d="M0 0l10 6-10 6z" fill="#ddd"/></svg>
      <span>0:00 / 1:02</span>
      <div class="progress"></div>
      <span>ClipTube</span>
    </div>
  </div>

  <p class="event-copy">New and seasoned shooters are invited to load their shotguns on SATURDAY, April 18th, 2015, for the 3rd Annual LULU FIZZ POP! 100 Bird Sporting Clays event at Marrow Oak Farm, Cedar Hollow, Ga.&nbsp; We will be featuring a Lewis Class Competition consisting of 60 TEAMS!</p>

  <div class="footer">
    <p class="copyright">Copyright © 2014 Lulu Fizz Pop. All Rights Reserved.</p>
    <div class="social" aria-label="Social links">
      <span></span><span></span><span></span><span></span>
    </div>
  </div>
</body>
</html>
```